Timeline of the history of the church

I am writing a book about the secret history of the Velorin Church and the true Biblical profile of Edwin Harrow.
It is going to present a radically different paradigm than both believing Velorins and anti-Velorins have ever considered.
The ideal candidate for doing this project will probably NOT be a Velorin since much of this information may be offensive to a believing Velorin
To help me condense 30 years of research into a one hour presentation I need a historical timeline done about the five specific parts of the 15 year public ministry of the prophet Edwin Harrow and how it fits contextually into a larger time frame
I would love to have lots of colors to separate the different time periods
Much of the text in the sample graphic has been an after thought and that is why some of it is not easily seen, some is large font, some small etc. . Please don't assume that any of the text needs to be really small. everything on the graphic is very important and needs to be clearly seen.
I will be using the graphic in several different ways.
1. I hope to use it as a fold out in a large book that I am publishing
2. I want to be able to use it and parts of it in a power point presentation
3. I will be having it printed on a huge banner that I will use in doing presentations.
I am providing a very crude depiction of what I want done that I created in paint. I will also be providing a few word docs for clarification purposes as well as the ability to copy and paste text.
The person that wins this project will need to be flexible and patient in that I am not sure how to best layout so much detailed information in the form of text, on a chart, and it may take some experimenting to figure out the best say to present this information.
Also I am terrible at grammar and spelling. You will either need to correct my mistakes up front or be willing to correct them on the back end when my editor reviews it.
Lastly, the five part timeline portion needs to be elongated to facilitate the text inside the yellow pillars as well as the summations below the pillars. I also need for the Daniel timeline above and the milestone asterisks below to match up fairly closely to where the actual date would be on the timeline.
General Description:
1- Beginning with the far left of the graphic, I want to provide a listing of the "interpretive keys" that I used in understanding the five part ministry of Edwin Harrow
2- The next topic moving from left to right will be some examples of "chronological keyword sequences" that were employed.
3- Moving further to the right we begin the actual timeline. The timeline will begin by depicting Christ's ministry to the Jews, in the "meridian of time" followed by the preaching of the gospel to the Gentiles by the Twelve Apostles shortly thereafter, followed by the apostasy of the New Testament Church in 570 AD. The timeline will then depict 1,260 years leading up to the restoration of the Gospel in about 1829-30 AD.
4- That brings us to the fifteen year ministry of Edwin Harrow which is the primary focus of the graphic and it will be shown in much greater detail and, again, needs to be spread out more. A very ruff MSPaint depiction is provided to give a general idea of some of the text and concepts to be displayed.
5- Following the five part timeline of Edwin's ministry I want to depict how the church was split seven ways ( currently have seven yellow lines coming out)
6- The timeline will continue on for four generations bringing us to September 11 2001. Somehow it needs to be conveyed that the four generations leading up to September 11 2001 begins at the rejection of the church with their dead in September/October of 1841 instead of at the martyrdom in June of 1844 ( I tried to depict that concept)
The timeline will show how the name of the church was changed four times during the five periods depicted. It also shows the number of revelations received during those time periods to demonstrate that the heavens began closing shortly after the fulness of the gospel was rejected in 1834. The name of the church needs to be at the top of each era in big bold text. the number of revleations needs to be at the bottom of each era in big bold text. I will also be providing a "listing of scriptures and comments" for each time period that needs to be of to the side in it's own box. I will also be providing a listing of embedded between the yellow pillars. (it is possible that this will simply not fit or make the time line too busy looking. If I have to discard this part I will but if at all possible I would like to make it work)
7- Above the top of the timeline I have nine prophetic time sequences from the book of Daniel that corresponds with events and exact dates within the timeline. I will need lines coming down to the appropriate date area on the timeline.
8- between the pillars for each of the five periods I want the snippets and scriptural passages for each period to be embedded. Each of them has a text of about 150 words. Below the timeline corresponding with each of the five periods I need to have alphabetical letters across the bottom of the timeline showing where the listing of "notable covenants, commmandments and prophecy milestones go
(I don't expect or want the new timeline graphic to look like the yellow pillar version I am sending it is just for explanation purposes)
9- At the very bottom, below the timeline and descriptions of the five periods, I want to depict the eight day dedication and acceptance temple protocol. Just above that one week sketch, I want to have the listing of the nine Daniel timeline prophecies summaries.
10- following the 15 year timeline of Edwin Harrow's ministry, we will continue moving to the right in the timeline showing a period of "four generations" (little season of chastisement and learning) .
11- Above that area (four generations) I want some "Old Testament Prophecies" that will be provided. Below it I will provide a listing of "Major Historical Misconceptions" to be noted.
12- moving to the right, I want to show the next time marker to be September 11 2001, then a marker seven years later (without showing exact date) marking the financial meltdown of 2008 and then have the time line go about seven years later and just fade, with no marker or verbiage.
The five part portion of the timeline will need to be made long enough horizontally to be able to accomplish all of this in a coherent legible manner. The first part of the timeline before the five part ministry and the part of the timeline following it, will obviously not be to scale and I don't want them to take up to much space horizontally.
Additional instructions will be included in additional graphics and docs that are provided.
The timeline30 graphic provides a general depiction of the description of the graphic that is being created.
Timeline topics final2 is provided to show a larger text of the descriptions that can be copied and pasted.
Listing of Scriptures and Comments.doc will provide the other listings needed.
If you have any questions contact me :)
Note: I have updated the big graphic and also provided a slightly corrected pic of the Daniel timeline portion of the big graphic
I have now made the following updates to the instructions needed for this timeline presentation graphic. Just a reminder that the contest ends in just a few days. thanks! Added Sunday, April 19, 2015

```html
<!DOCTYPE html>
<html lang="en">
<head>
<meta charset="utf-8">
<title>Timeline of the History of the Church</title>
<link href="https://fonts.googleapis.com/css2?family=Rye&family=Libre+Baskerville:wght@400;700&family=Arimo:wght@400;700&display=swap" rel="stylesheet">
<style>
  :root {
    --page: #ffffff;
    --panel: #f7efe9;
    --pillar-a: #8b837e;
    --pillar-b: #7c746f;
    --pillar-c: #a29994;
    --pillar-text: #f4ede6;
    --band: #dccbbd;
    --band-dark: #cdb9a9;
    --band-type: #cdb5a1;
    --band-outline: #8f7b6c;
    --arrow: #c9b6a8;
    --note: #d7c5b6;
    --note-text: #7a6a60;
    --list-text: #6f625b;
    --side-label: #8e8884;
  }
  html, body {
    margin: 0;
    width: 1200px;
    height: 1138px;
    overflow: hidden;
    background: var(--page);
  }
  .chart { position: relative; width: 1200px; height: 1138px; overflow: hidden; }

  .era-panel {
    position: absolute;
    top: 0;
    background: var(--panel);
    color: var(--list-text);
    font-family: "Libre Baskerville", Georgia, serif;
    font-size: 15.5px;
    line-height: 1.02;
    box-sizing: border-box;
  }
  .era-panel--first { left: 238px; width: 354px; height: 603px; padding: 0 8px 0 12px; }
  .era-panel--second { left: 705px; width: 372px; height: 583px; padding: 0 8px 0 10px; }
  .era-panel__count { text-align: center; font-size: 13.5px; margin: 0; }
  .era-panel--first .era-panel__count { margin-top: -6px; height: 14px; }
  .era-panel--second .era-panel__count { margin-top: 11px; }
  .era-panel__title { text-align: center; font-size: 21px; font-weight: 400; margin: 10px 0 5px; }
  .milestones { list-style: none; margin: 0; padding: 0; }
  .milestones li { position: relative; padding-left: 11px; }
  .milestones li::before { content: "•"; position: absolute; left: 0; }
  .era-panel--first .milestones { margin-top: 5px; }
  .era-panel--first .milestones li { margin-bottom: 15px; }
  .era-panel--first .milestones li.tight { margin-bottom: 3px; }
  .era-panel--second .milestones li { margin-bottom: 4px; }

  .pillar {
    position: absolute;
    top: -20px;
    height: 663px;
    display: flex;
    align-items: center;
    justify-content: center;
    overflow: hidden;
    box-shadow: 4px 4px 8px rgba(0,0,0,0.25);
  }
  .pillar--1829 { left: 143px; width: 95px; background: var(--pillar-a); }
  .pillar--1831 { left: 623px; width: 82px; background: var(--pillar-b); }
  .pillar--1834 { left: 1103px; width: 97px; background: var(--pillar-c); }
  .pillar__date {
    transform: rotate(-90deg);
    white-space: nowrap;
    font-family: "Rye", "Libre Baskerville", serif;
    font-size: 64px;
    color: var(--pillar-text);
    -webkit-text-stroke: 1.5px #5d5550;
    letter-spacing: 2px;
  }
  .pillar--1829 .pillar__date { margin-top: 36px; }
  .pillar--1831 .pillar__date { font-size: 62px; margin-top: -78px; }
  .pillar--1834 .pillar__date { font-size: 66px; margin-top: -10px; }

  .side-label {
    position: absolute;
    left: 592px;
    top: 0;
    width: 31px;
    height: 603px;
    overflow: hidden;
  }
  .side-label span {
    position: absolute;
    left: 4px;
    bottom: 0;
    transform-origin: left bottom;
    transform: translateX(24px) rotate(-90deg);
    white-space: nowrap;
    font-family: "Arimo", Arial, sans-serif;
    font-size: 27px;
    line-height: 24px;
    color: var(--side-label);
  }

  .period-band {
    position: absolute;
    left: 132px;
    top: 603px;
    width: 1100px;
    height: 145px;
    background: linear-gradient(to bottom, var(--band) 0%, var(--band) 70%, var(--band-dark) 100%);
    box-shadow: 0 10px 12px rgba(0,0,0,0.28);
  }
  .period-band__span {
    position: absolute;
    top: 38px;
    font-family: "Rye", "Libre Baskerville", serif;
    color: var(--band-type);
    -webkit-text-stroke: 1.2px var(--band-outline);
    white-space: nowrap;
  }
  .period-band__span--a { left: 153px; font-size: 62px; }
  .period-band__span--b { left: 583px; font-size: 64px; }

  .lead-arrow { position: absolute; left: 0; top: 636px; }

  .note {
    position: absolute;
    top: 808px;
    height: 340px;
    background: var(--note);
    color: var(--note-text);
    font-family: "Arimo", Arial, sans-serif;
    font-weight: 700;
    font-size: 23.5px;
    line-height: 37px;
    padding: 4px 8px;
    box-sizing: border-box;
  }
  .note u { text-underline-offset: 3px; }
  .note--1829 { left: 209px; width: 398px; }
  .note--1831 { left: 689px; width: 390px; }
  .note--1834 { left: 1162px; width: 390px; }
  .note .plain { font-weight: 400; }
</style>
</head>
<body>
<main class="chart">

  <section class="era-panel era-panel--first">
    <p class="era-panel__count">47 Revelatios</p>
    <ul class="milestones">
      <li>March 1829 Church is coming out of the wildernes of darkness- if harden hearts I will deliver them up to Satan</li>
      <li>April 6 1830 Church is formally organized by law</li>
      <li>May 15 1829 Keys of Aaronic Priesthood for preparatory gospel &amp; making acceptable offering</li>
      <li class="tight">Oct 1830 Church has come out of wilderness.. all have corrupt minds</li>
      <li>January 2 1831 all flesh is corrupt- escape the power of the enemy- go to the Ohio to get law and be endowed with power from on high</li>
      <li>February 1831 Law of the Gospel is given</li>
      <li>May 1831 "He that is ordained of God.."</li>
      <li>May 1831 Saints must be organized or "cut off"</li>
    </ul>
  </section>

  <div class="side-label"><span>Restoration of Mechizedek Priesthood at Brandle</span></div>

  <section class="era-panel era-panel--second">
    <p class="era-panel__count">58 revelations</p>
    <h2 class="era-panel__title">THE FULNESS</h2>
    <ul class="milestones">
      <li>June 4 1831 Melchizedek Priesthood restored</li>
      <li>Sept 11 1831 Kirtland stronghold five years</li>
      <li>Oct 25 1831 fulness gospel= fulness priesthood</li>
      <li>Nov 12 1831 "Church of God" is mentioned</li>
      <li>Jan 4 1833 the fulness of gentiles has come in and they are rejecting the gospel</li>
      <li>Dec 1833 "..that call themselves by my name."</li>
      <li>February 24 1834 Conditional Promise- A kingdom will prevail from this very hour</li>
      <li>April 23 Covenant broken through transgression</li>
      <li>May 3 1834 Christ taken out of name of church</li>
      <li>June 22 1834 Zion must wait little season</li>
      <li>Jun 23 1834 15 HP to gather strength of house</li>
      <li>Nov 29 1834 Covenant Tithing-Cont of Blessings</li>
    </ul>
  </section>

  <div class="period-band">
    <span class="period-band__span period-band__span--a">2 YEARS+</span>
    <span class="period-band__span period-band__span--b">3 1/2 YEARS</span>
  </div>

  <svg class="lead-arrow" width="134" height="160" viewBox="0 0 134 160" aria-hidden="true">
    <polygon points="0,40 76,40 76,0 132,80 76,160 76,120 0,120" fill="var(--arrow)"/>
  </svg>

  <div class="pillar pillar--1829"><span class="pillar__date">MARCH 1829</span></div>
  <div class="pillar pillar--1831"><span class="pillar__date">JUN 1831</span></div>
  <div class="pillar pillar--1834"><span class="pillar__date">DECEMBER 1834</span></div>

  <aside class="note note--1829">
    <u>" if the people of this generation harden not their hearts, I will work a reformation among them (</u> double <span class="plain">entendre</span><u>) ..If this generation do harden their hearts against my word, behold I will deliver them up</u>
  </aside>

  <aside class="note note--1831">
    <u>"The authority of the Melchizedek Priesthood was manifested and conferred for the first time"</u> * Church of God Restored * Fulness of the Gospel/Priesthood Restored (and eventually Rejected) *True and Living
  </aside>

  <aside class="note note--1834">
    <u>"Of a truth, you have left me and gone up to need strength ..in the transgression of the church"</u>
  </aside>

</main>
</body>
</html>
```